Ward Compass Business Card Design*

We need a business card design for our company Ward Compass. Our company is specialized in providing online consulting services regarding medical institutions, hospitals and doctors. We work with patients worldwide looking to choose between healthcare providers. We have a website you may use as a reference, where we list doctors and clinics worldwide. So we target Medical providers as well as patients worldwide.
Target Market(s)
Medical Providers and patients around the world
Industry/Entity Type
Medical
Contact Information for Business Card
Salma Derkaoui
CEO
+90 612 348 2071
info@wardcompass-example.com
www.wardcompass-example.com
14 Annakhil 3 H.R.B. Rabat, Morocco
Requirements
Must have
- Company logo/name on one full side, personal info and smaller logo and company name on the other side.
Nice to have
- Smart and elegant design

```html
<!DOCTYPE html>
<html lang="en">
<head>
<meta charset="utf-8">
<title>Ward Compass Business Card</title>
<link rel="stylesheet" href="https://fonts.googleapis.com/css2?family=Montserrat:wght@400;600;700&family=Lato:wght@400&display=swap">
<style>
  :root {
    --bg: #2f2f2f;
    --paper: #ffffff;
    --blue-deep: #2c6db6;
    --blue-bright: #33a3da;
    --blue-mid: #2f86c9;
    --ink: #3a3a3a;
    --rule: #cfcfcf;
  }
  html, body {
    margin: 0;
    padding: 0;
    width: 1200px;
    height: 866px;
    overflow: hidden;
    background: var(--bg);
  }
  .canvas {
    position: relative;
    width: 1200px;
    height: 866px;
  }
  .card {
    position: absolute;
    left: 250px;
    width: 700px;
    height: 400px;
    overflow: hidden;
    box-shadow: 0 10px 28px rgba(0,0,0,0.45);
  }
  .card--front { top: 22px; background: var(--paper); }
  .card--back {
    top: 444px;
    background: linear-gradient(160deg, var(--blue-bright) 0%, var(--blue-deep) 100%);
  }

  /* Front side */
  .person {
    position: absolute;
    left: 60px;
    top: 140px;
  }
  .person__name {
    margin: 0;
    font-family: "Montserrat", sans-serif;
    font-size: 22px;
    letter-spacing: 0.5px;
    text-transform: uppercase;
  }
  .person__first { font-weight: 700; color: var(--blue-deep); }
  .person__last { font-weight: 400; color: var(--blue-mid); }
  .person__role {
    margin: 2px 0 0;
    font-family: "Montserrat", sans-serif;
    font-size: 15px;
    color: var(--ink);
  }
  .contact {
    list-style: none;
    margin: 22px 0 0;
    padding: 0;
    font-family: "Lato", sans-serif;
    font-size: 16px;
    color: var(--ink);
  }
  .contact__item {
    display: flex;
    align-items: center;
    gap: 8px;
    margin-bottom: 6px;
  }
  .contact__icon { width: 15px; height: 15px; fill: var(--blue-deep); }

  .divider {
    position: absolute;
    left: 130px;
    right: 60px;
    top: 292px;
    height: 1px;
    background: var(--rule);
  }

  .brand {
    position: absolute;
    display: flex;
    align-items: center;
    gap: 12px;
    font-family: "Montserrat", sans-serif;
    font-weight: 600;
    text-transform: uppercase;
    white-space: nowrap;
  }
  .brand--front {
    left: 330px;
    top: 104px;
    font-size: 27px;
    letter-spacing: 1px;
    color: var(--blue-mid);
  }
  .brand__dot {
    flex: none;
    border-radius: 50%;
    box-sizing: border-box;
  }
  .brand--front .brand__dot {
    width: 40px;
    height: 40px;
    border: 7px solid var(--blue-mid);
  }

  .website {
    position: absolute;
    right: 60px;
    bottom: 48px;
    margin: 0;
    font-family: "Lato", sans-serif;
    font-size: 16px;
    color: var(--blue-mid);
  }

  .edge-band {
    position: absolute;
    left: 0;
    right: 0;
    bottom: 0;
    height: 10px;
    background: linear-gradient(90deg, var(--blue-deep) 0%, var(--blue-deep) 42%, var(--blue-bright) 42%, var(--blue-bright) 100%);
  }

  /* Back side */
  .brand--back {
    left: 50%;
    top: 50%;
    transform: translate(-50%, -50%);
    font-size: 38px;
    letter-spacing: 1.5px;
    color: var(--paper);
    gap: 16px;
  }
  .brand--back .brand__dot {
    width: 60px;
    height: 60px;
    border: 10px solid var(--paper);
  }
</style>
</head>
<body>
<main class="canvas">

  <section class="card card--front" aria-label="Business card, front">
    <div class="person">
      <h1 class="person__name"><span class="person__first">Salma</span> <span class="person__last">Derkaoui</span></h1>
      <p class="person__role">CEO</p>
      <ul class="contact">
        <li class="contact__item">
          <svg class="contact__icon" viewBox="0 0 24 24" aria-hidden="true"><path d="M6.6 10.8a15.1 15.1 0 0 0 6.6 6.6l2.2-2.2a1 1 0 0 1 1-.25 11.4 11.4 0 0 0 3.6.57 1 1 0 0 1 1 1V20a1 1 0 0 1-1 1A17 17 0 0 1 3 4a1 1 0 0 1 1-1h3.5a1 1 0 0 1 1 1c0 1.25.2 2.45.57 3.57a1 1 0 0 1-.25 1z"/></svg>
          <span>+90 612 348 2071</span>
        </li>
        <li class="contact__item">
          <svg class="contact__icon" viewBox="0 0 24 24" aria-hidden="true"><path d="M2 5h20v14H2z M3.5 6.5 12 13l8.5-6.5" fill="var(--blue-deep)" stroke="#fff" stroke-width="1.5"/></svg>
          <span>info@wardcompass-example.com</span>
        </li>
      </ul>
    </div>

    <div class="brand brand--front">
      <span class="brand__dot" aria-hidden="true"></span>
      <span class="brand__name">Ward Compass</span>
    </div>

    <div class="divider" aria-hidden="true"></div>
    <p class="website">www.wardcompass-example.com</p>
    <div class="edge-band" aria-hidden="true"></div>
  </section>

  <section class="card card--back" aria-label="Business card, back">
    <div class="brand brand--back">
      <span class="brand__dot" aria-hidden="true"></span>
      <span class="brand__name">Ward Compass</span>
    </div>
  </section>

</main>
</body>
</html>
```